Information flyer for 5 day treatment flyer

I am wanting a double sided flyer for my next 5 day treatment program for addictions. I have included the copy for the flyer as an attachment.
I have also included a drop box link to my brand guidelines and my logos. The logo I prefer is the grey horse with the words Willowmere Collective under.
https://www.filecrate.example/sh/k2jtq7wn3xb5lp1/BBQr9TzLm4Kd7c8NpWvY2hsXe?dl=0

https://www.filecrate.example/s/qm8vz2kt6bw9rc4/WILLOWMERE%20COLLECTIVE%20%7C%20Brand%20Identity%20Guidelines.pdf?dl=0
I have also included a copy of an existing flyer which I like very much and a documant with the copy.
https://www.filecrate.example/sh/t7wbn3kx9zq1mv5/CCRt2pLw8-nZ4Kj7FyTuGHs_b?dl=0

I prefer simple, elegant designs please. The design needs to show my clients that I know what I am doing and I am trust worthy and a skilled professional.

Here is the drop box link to the images I have selected for this program. The tones in the images I have selected are orange/red. Please feel free to pick what you think works well.
https://www.filecrate.example/sh/mrq5jv82lnc0tfw/DDDhW392Bx6Lp88_Q7KcZnRye?dl=0

Many thanks
Marisol

```html
<!DOCTYPE html>
<html lang="en">
<head>
<meta charset="utf-8">
<title>5 Day Intensive Treatment Program – Behind Closed Doors</title>
<link rel="stylesheet" href="https://fonts.googleapis.com/css2?family=Roboto:wght@400;500;700;900&family=Open+Sans:wght@400;700&display=swap">
<style>
  :root {
    --navy: #0e2537;
    --navy-deep: #0b1f2e;
    --cream: #f1ecc6;
    --white: #ffffff;
    --ink: #14110f;
    --orange: #f2692a;
    --red: #e51f2f;
    --band: #1c0f0d;
    --logo-grey: #9aa0a6;
  }
  * { margin: 0; padding: 0; box-sizing: border-box; }
  html, body { width: 848px; height: 1200px; overflow: hidden; background: var(--navy); }
  .flyer {
    position: relative; width: 848px; height: 1200px; overflow: hidden;
    background: var(--navy); font-family: "Roboto", Arial, sans-serif;
  }

  /* Header */
  .header { position: absolute; left: 0; top: 0; width: 848px; height: 94px; background: var(--navy); }
  .header__title { position: absolute; left: 10px; top: 0; width: 530px; text-align: center; white-space: nowrap; }
  .header__kicker { color: var(--cream); font-size: 39px; font-weight: 400; line-height: 44px; }
  .header__name { color: var(--white); font-size: 37px; font-weight: 700; line-height: 44px; letter-spacing: 0.5px; }
  .header__divider { position: absolute; left: 552px; top: 0; width: 5px; height: 94px; background: var(--white); }
  .header__days {
    position: absolute; left: 598px; top: -2px; color: var(--cream);
    font-size: 88px; font-weight: 400; line-height: 96px; white-space: nowrap;
  }
  .rule { position: absolute; left: 0; top: 94px; width: 848px; height: 4px; background: var(--white); }
  .subtitle {
    position: absolute; left: 0; top: 98px; width: 848px; height: 54px;
    background: var(--navy); color: var(--white); white-space: nowrap;
    font-family: "Open Sans", Arial, sans-serif; font-size: 21.4px; line-height: 54px; text-align: center;
  }

  /* Photo area */
  .hero {
    position: absolute; left: 0; top: 152px; width: 848px; height: 870px;
    background:
      radial-gradient(ellipse 330px 320px at 470px 560px, rgba(40,14,16,0.92) 0%, rgba(60,20,18,0.75) 45%, rgba(60,20,18,0) 100%),
      linear-gradient(180deg, rgba(0,0,0,0) 60%, rgba(50,16,14,0.9) 76%, rgba(20,10,12,0.98) 100%),
      radial-gradient(ellipse 200px 190px at 170px 520px, rgba(255,252,232,1), rgba(255,238,200,0) 100%),
      linear-gradient(90deg, rgba(225,100,60,0.45) 0%, rgba(0,0,0,0) 35%, rgba(0,0,0,0) 70%, rgba(60,20,24,0.45) 100%),
      linear-gradient(180deg, #c98468 0%, #eab394 18%, #f8dcc0 38%, #fbe8cc 52%, #eaa67e 66%, #b04a32 78%, #2a1216 100%);
  }

  .intimacy { position: absolute; left: 8px; top: 172px; width: 300px; }
  .intimacy__heading { font-size: 23px; font-weight: 700; color: var(--white); line-height: 28px; letter-spacing: 0.3px; }
  .intimacy__heading em { font-style: normal; color: var(--orange); }
  .intimacy__body {
    margin-top: 4px; font-size: 15.5px; font-weight: 700; line-height: 14.4px; color: var(--ink);
  }
  .intimacy__body span { color: var(--red); }

  .hunger { position: absolute; left: 404px; top: 168px; width: 444px; text-align: center; }
  .hunger__heading { font-size: 21px; font-weight: 700; color: var(--navy-deep); line-height: 28px; }
  .hunger__heading em { font-style: normal; color: var(--red); }
  .hunger__body { margin-top: 4px; font-size: 15.3px; font-weight: 500; color: var(--ink); line-height: 18.5px; white-space: nowrap; }

  .focus {
    position: absolute; left: -4px; top: 836px; width: 340px; text-align: center;
    font-size: 26px; font-weight: 700; line-height: 20.5px; color: var(--cream); letter-spacing: 0.2px;
  }

  /* Question band */
  .question {
    position: absolute; left: 0; top: 1022px; width: 848px; height: 54px;
    background: var(--band); color: var(--white); text-align: center;
    font-size: 15.5px; font-weight: 700; line-height: 14.5px; padding-top: 8px;
  }

  /* Footer */
  .footer { position: absolute; left: 0; top: 1076px; width: 848px; height: 124px; background: var(--navy); }
  .footer__lead {
    position: absolute; left: 0; top: 10px; width: 692px; text-align: center;
    font-family: "Open Sans", Arial, sans-serif; font-size: 19px; font-weight: 700; color: var(--white); line-height: 24px;
  }
  .footer__text {
    position: absolute; left: 24px; top: 44px; width: 644px; text-align: center; white-space: nowrap;
    font-family: "Open Sans", Arial, sans-serif; font-size: 12.6px; color: var(--white); line-height: 14.4px;
  }
  .brand { position: absolute; left: 700px; top: 32px; width: 148px; text-align: center; }
  .brand__dot { display: block; margin: 0 auto 22px; width: 40px; height: 40px; border-radius: 50%; background: var(--logo-grey); }
  .brand__name { font-family: "Open Sans", Arial, sans-serif; font-size: 8.5px; color: var(--logo-grey); letter-spacing: 1.4px; white-space: nowrap; }
</style>
</head>
<body>
<main class="flyer">
  <header class="header">
    <div class="header__title">
      <p class="header__kicker">Intensive treatment program</p>
      <h1 class="header__name">BEHIND CIOSED DOORS</h1>
    </div>
    <div class="header__divider"></div>
    <p class="header__days">5 DAY</p>
  </header>
  <div class="rule"></div>
  <p class="subtitle">Break destructive relationship patterns and learn How to create more love intimacy</p>

  <div class="hero" role="img" aria-label="Silhouette of a couple sitting back to back on grass against an orange-red sunset sky"></div>

  <section class="intimacy">
    <h2 class="intimacy__heading">WHAT IS <em>INTIMACY?</em></h2>
    <p class="intimacy__body">Intimacy is our emotional<br>food it sustains and<br>nourishes us,helping us<br>feel connected,understood<br>in our most important<br>relationships creates<br>problems<br>such as<br><span>Anxiety,jealousl,withdrawal,<br>betrayal,abandonment and<br>even infidelity.</span></p>
  </section>

  <section class="hunger">
    <h2 class="hunger__heading">HUNGER VERSUS <em>LOVE</em></h2>
    <p class="hunger__body">Emotional hunger is not love.This is strong need casued<br>by emotional deprivation in childhood.Feeling of<br>emotional hunger are experienced as deep internal<br>sensations.That range in intensity from a dull ache to<br>sharp painful feeling.This emotional intensity is often<br>confused with real love.Many people claim to be loving<br>and caring,when in fact they are actually feeling their<br>emotional hunger and neediness.Emotional hunger is<br>what we experience when feeling abandonment pain.This<br>keeps using unfulfilling,Destructive add addictive<br>relationships.</p>
  </section>

  <p class="focus">THIS PROGRAM FOCUSES<br>ON ABANDONEMENT AND<br>ENGULFMENT ISSUES.</p>

  <p class="question">WHY IS IT IMPOTANT TO EXAMINE OUR CHILDHOOD<br>WHEN TRYING TO SORT OUT OUR ISSUES IN ADULT RELATIONSHIP<br>TODAY?</p>

  <footer class="footer">
    <p class="footer__lead">Children are needy by nature,not by choice.</p>
    <p class="footer__text">They instinctively adapt their behaviour and personalities in order to get their emotional needs met.<br>As a result of the fantasy bond,created betwwen child and caregiver, we carry with us into adulthood<br>the same survival mechanisms leading to a sacrifice of our freedom and any real intimacy in loving<br>relationships.Instead,we create dependencies with people substances and behaviour patterns to fill<br>the deep emptiness or loneliness within us.</p>
    <div class="brand">
      <span class="brand__dot"></span>
      <p class="brand__name">WILLOWMERE COLLECTIVE</p>
    </div>
  </footer>
</main>
</body>
</html>
```